New Business Card Design for Engineering and Surveying Company

We need a new design template for our business cards. We are a civil engineering, land surveying and pipeline integrity business. Please see dkhpartners.com for details. We need a bold, new business card design to complement our rebranding and marketing program. We have anew logo and attached vectro file. Please find additional details below. I am available to answer any questions.

Target Market(s)

Contractors, business owners, oil companies

Contact Information for Business Card

Needs to be customizable for different people (name, title, cell)

Font styles to use
Sans Serif
Other font styles liked:
• See eps file

Requirements
Must have
• Example Information:
Trevor Ashcombe

T:409-555-0173
M: 202-555-0148
tashcombe@dkhprtnrs.com

Address: 1875 Pinecrest Parkway, Marlow Creek, Texas 77871
Email: tolvanrey@dkhpartners.com
Website: www.dkhpartners.com
Nice to have
• I would like the back of the card to have the logo on a bold background with the text below:

[logo]
DORAN KESSLING & PARTNERS
CIVIL ENGINEERING | LAND SURVEYING | PIPELINE INTEGRITY

The reverse side should have the contact information for the person (example above), a smaller version of the logo and a graphic

```html
<!DOCTYPE html>
<html lang="en">
<head>
<meta charset="utf-8">
<title>Doran Kessling &amp; Partners — Business Cards</title>
<link href="https://fonts.googleapis.com/css2?family=PT+Sans:wght@400;700&display=swap" rel="stylesheet">
<style>
  :root {
    --backdrop: #e6e7ea;
    --card: #ffffff;
    --brand-red: #ec1c2c;
    --brand-blue: #1d4fa8;
    --ink: #111317;
    --on-red: #ffffff;
  }
  * { box-sizing: border-box; margin: 0; padding: 0; }
  html, body {
    width: 1200px; height: 900px; overflow: hidden;
    background: var(--backdrop);
    font-family: "PT Sans", Arial, sans-serif;
  }
  .canvas { position: relative; width: 1200px; height: 900px; }
  .card {
    position: absolute; left: 320px;
    width: 560px; height: 320px;
    background: var(--card);
    border-radius: 26px;
    overflow: hidden;
    box-shadow: 0 6px 18px rgba(0,0,0,.14);
  }
  .card--front { top: 90px; }
  .card--back { top: 490px; }
  .card__shapes { position: absolute; inset: 0; width: 100%; height: 100%; }

  .wordmark {
    position: absolute; display: flex; align-items: center; gap: 10px;
    color: var(--ink); font-weight: 700; letter-spacing: .02em;
    white-space: nowrap;
  }
  .wordmark__square { width: 18px; height: 18px; background: var(--brand-red); flex: none; }
  .card--front .wordmark { left: 130px; top: 112px; font-size: 24px; }
  .card--front .website {
    position: absolute; left: 130px; top: 178px;
    font-size: 20px; color: var(--brand-blue);
  }
  .website__domain { color: var(--brand-red); font-weight: 700; }

  .card--back .wordmark { right: 34px; top: 34px; font-size: 19px; }
  .person {
    position: absolute; left: 30px; top: 178px; width: 190px;
    color: var(--on-red); text-align: right;
  }
  .person__name { font-size: 22px; font-weight: 700; line-height: 1.1; }
  .person__title { font-size: 13px; margin-top: 4px; }
  .divider {
    position: absolute; left: 236px; top: 150px; width: 2px; height: 142px;
    background: var(--on-red);
  }
  .contacts {
    position: absolute; left: 252px; top: 152px;
    list-style: none; color: var(--on-red); font-size: 12.5px; line-height: 1.25;
  }
  .contacts li { display: flex; align-items: flex-start; gap: 8px; margin-bottom: 5px; white-space: nowrap; }
  .contacts svg { width: 13px; height: 13px; flex: none; margin-top: 1px; fill: var(--on-red); }
</style>
</head>
<body>
<main class="canvas">

  <section class="card card--front" aria-label="Business card front">
    <svg class="card__shapes" viewBox="0 0 560 320" preserveAspectRatio="none" aria-hidden="true">
      <path d="M0 0 H120 C40 70 40 250 120 320 H0 Z" fill="var(--brand-red)"/>
      <path d="M560 170 C520 230 480 285 440 320 H560 Z" fill="var(--brand-blue)"/>
    </svg>
    <div class="wordmark"><span class="wordmark__square"></span>DORAN KESSLING &amp; PARTNERS</div>
    <p class="website">www.<span class="website__domain">dkhpartners</span>.com</p>
  </section>

  <section class="card card--back" aria-label="Business card back">
    <svg class="card__shapes" viewBox="0 0 560 320" preserveAspectRatio="none" aria-hidden="true">
      <path d="M0 170 C0 140 20 125 50 125 H470 C490 125 500 140 500 160 V280 C500 305 485 320 460 320 H0 Z" fill="var(--brand-red)"/>
    </svg>
    <div class="wordmark"><span class="wordmark__square"></span>DORAN KESSLING &amp; PARTNERS</div>

    <div class="person">
      <p class="person__name">Trevor Ashcombe</p>
      <p class="person__title">Founder &amp; Director</p>
    </div>
    <div class="divider"></div>

    <ul class="contacts">
      <li><svg viewBox="0 0 24 24"><path d="M4 4h5l2 5-3 2a12 12 0 0 0 5 5l2-3 5 2v5a2 2 0 0 1-2 2A18 18 0 0 1 2 6a2 2 0 0 1 2-2z"/></svg>409-555-0173</li>
      <li><svg viewBox="0 0 24 24"><path d="M7 1h10a2 2 0 0 1 2 2v18a2 2 0 0 1-2 2H7a2 2 0 0 1-2-2V3a2 2 0 0 1 2-2zm0 3v14h10V4zm5 15.5a1.2 1.2 0 1 0 0 2.4 1.2 1.2 0 0 0 0-2.4z"/></svg>202-555-0148</li>
      <li><svg viewBox="0 0 24 24"><path d="M2 5h20v14H2zm2 2v.5l8 5.5 8-5.5V7zm0 2.9V17h16V9.9l-8 5.5z"/></svg>tashcombe@dkhprtnrs.com</li>
      <li><svg viewBox="0 0 24 24"><path d="M12 2a10 10 0 1 0 0 20 10 10 0 0 0 0-20zm1 2.1c1.5 1.6 2.5 4 2.8 6.9H13zM11 4.1V11H8.2c.3-2.9 1.3-5.3 2.8-6.9zM4.1 13h2.1c.1 2.2.6 4.2 1.5 5.8A8 8 0 0 1 4.1 13zm0-2a8 8 0 0 1 3.6-5.8C6.8 6.8 6.3 8.8 6.2 11zM11 19.9c-1.5-1.6-2.5-4-2.8-6.9H11zm2 0V13h2.8c-.3 2.9-1.3 5.3-2.8 6.9zm3.3-1.1c.9-1.6 1.4-3.6 1.5-5.8h2.1a8 8 0 0 1-3.6 5.8zM17.8 11c-.1-2.2-.6-4.2-1.5-5.8A8 8 0 0 1 19.9 11z"/></svg>www.dkhpartners.com</li>
      <li><svg viewBox="0 0 24 24"><path d="M12 1a8 8 0 0 0-8 8c0 6 8 14 8 14s8-8 8-14a8 8 0 0 0-8-8zm0 11a3 3 0 1 1 0-6 3 3 0 0 1 0 6z"/></svg>1875 Pinecrest Parkway, Marlow Creek,<br>Texas 77871</li>
    </ul>
  </section>

</main>
</body>
</html>
```